Lounge Bar Menu

We need an elegant Bar Menu for ou Lounge Bar.
Logo attached.
We already have the support. A cover like a book in A5 format.
Attached as well our menu.

Industry/Entity Type

Bar, Hotel4*

```html
<!DOCTYPE html>
<html lang="en">
<head>
<meta charset="UTF-8">
<title>Marino Lounge Bar – Menu Cover</title>
<link rel="stylesheet" href="https://fonts.googleapis.com/css2?family=Josefin+Sans:wght@300&family=Oswald:wght@600&display=swap">
<style>
  :root {
    --board-dark: #232323;
    --board-mid: #363636;
    --gold: #d4a24c;
    --ink: #ffffff;
  }
  * { margin: 0; padding: 0; box-sizing: border-box; }
  html, body {
    width: 848px;
    height: 1200px;
    overflow: hidden;
    background: var(--board-dark);
  }
  .cover {
    position: relative;
    width: 848px;
    height: 1200px;
    overflow: hidden;
  }
  .drink-pattern {
    position: absolute;
    inset: 0;
    background: radial-gradient(ellipse at 50% 50%, var(--board-mid) 0%, #2c2c2c 55%, var(--board-dark) 100%);
  }
  .rule-pair {
    position: absolute;
    left: 204px;
    width: 440px;
    height: 11px;
    border-top: 1.4px solid var(--gold);
    border-bottom: 1.4px solid var(--gold);
  }
  .rule-pair--top-upper { top: 226px; }
  .rule-pair--top-lower { top: 390px; }
  .rule-pair--bottom { top: 1068px; }
  .brand {
    position: absolute;
    left: 0;
    width: 848px;
    text-align: center;
    font-family: "Josefin Sans", sans-serif;
    font-weight: 300;
    color: var(--ink);
    line-height: 1;
    white-space: nowrap;
  }
  .brand__name {
    top: 280px;
    font-size: 62px;
    letter-spacing: 9px;
    padding-left: 9px;
  }
  .brand__tagline {
    top: 346px;
    font-size: 18px;
    letter-spacing: 4px;
    padding-left: 4px;
  }
  .cover__title {
    position: absolute;
    left: 0;
    top: 636px;
    width: 848px;
    text-align: center;
    font-family: "Oswald", sans-serif;
    font-weight: 600;
    font-size: 113px;
    line-height: 1;
    letter-spacing: -1px;
    color: var(--ink);
  }
</style>
</head>
<body>
<main class="cover">
  <div class="drink-pattern" role="img" aria-label="Chalkboard background with a faint hand-drawn pattern of cocktails, smoothies and drinks with straws"></div>

  <div class="rule-pair rule-pair--top-upper" role="img" aria-label="Gold double divider line with decorative arrow ends"></div>

  <p class="brand brand__name">MARINO</p>
  <p class="brand brand__tagline">LOUNGE - BAR</p>

  <div class="rule-pair rule-pair--top-lower" role="img" aria-label="Gold double divider line with decorative arrow ends"></div>

  <h1 class="cover__title">Menu</h1>

  <div class="rule-pair rule-pair--bottom" role="img" aria-label="Gold double divider line with decorative arrow ends"></div>
</main>
</body>
</html>
```